business card and stationary pest control company
Bugwarden
business card and stationary pest control company - Cleaning
Creative Brief
Bright & Fun-filled
Malcolm Teague
General Manager
to be added
info@bugwarden.example
bugwarden.example
tarloq tarloq
Hi guys, please bear in mind it's a full stationary project, letterhead, fax, email, envelope etc ...
ravenmoss ravenmoss
check your private messages on top right! thankyou

```html
<!DOCTYPE html>
<html lang="en">
<head>
<meta charset="utf-8">
<title>Bugwarden business card</title>
<link rel="stylesheet" href="https://fonts.googleapis.com/css2?family=Montserrat:wght@400;600;700&family=Open+Sans:wght@400;600&display=swap">
<style>
  :root {
    --stage: #d9d9db;
    --paper: #ffffff;
    --brand-blue: #1f3f9e;
    --brand-red: #e3241b;
    --ink: #4a4a4a;
    --ink-soft: #6d6d6d;
  }
  * { margin: 0; padding: 0; box-sizing: border-box; }
  html, body { width: 1200px; height: 895px; overflow: hidden; }
  body {
    background: var(--stage);
    font-family: "Open Sans", Arial, sans-serif;
    color: var(--ink);
    position: relative;
  }
  .card {
    position: absolute;
    left: 250px;
    width: 700px;
    height: 400px;
    background: var(--paper);
    overflow: hidden;
    box-shadow: 0 6px 18px rgba(0,0,0,.18);
  }
  .card--front { top: 35px; }
  .card--back { top: 460px; }
  .card svg.bands { position: absolute; inset: 0; }

  .brand {
    position: absolute;
    display: flex;
    align-items: center;
    gap: 12px;
  }
  .brand__dot {
    width: 34px; height: 34px;
    border-radius: 50%;
    background: var(--brand-red);
  }
  .brand__name {
    font-family: "Montserrat", Arial, sans-serif;
    font-weight: 700;
    color: var(--brand-blue);
    letter-spacing: -0.5px;
  }
  .card--front .brand { left: 50%; top: 172px; transform: translateX(-50%); }
  .card--front .brand__name { font-size: 46px; }
  .card--front .brand__dot { width: 44px; height: 44px; }

  .card--back .brand { left: 40px; top: 38px; }
  .card--back .brand__name { font-size: 34px; }

  .person {
    position: absolute;
    right: 40px; top: 102px;
    text-align: right;
  }
  .person__name {
    font-family: "Montserrat", Arial, sans-serif;
    font-weight: 600;
    font-size: 19px;
    letter-spacing: 1px;
    color: var(--ink);
  }
  .person__role {
    font-size: 10px;
    letter-spacing: 1.5px;
    color: var(--ink-soft);
    margin-top: 2px;
  }
  .contact {
    position: absolute;
    top: 242px;
    font-size: 14px;
    line-height: 24px;
    color: var(--ink);
  }
  .contact--web { left: 40px; }
  .contact--address { left: 270px; }
  .contact--phone { right: 40px; text-align: right; }
</style>
</head>
<body>

<section class="card card--front" aria-label="Business card front">
  <svg class="bands" width="700" height="400" viewBox="0 0 700 400" aria-hidden="true">
    <rect x="0" y="40" width="700" height="58" fill="var(--brand-blue)"/>
    <polyline points="340,40 368,69 340,98" fill="none" stroke="var(--paper)" stroke-width="7"/>
    <rect x="0" y="302" width="700" height="58" fill="var(--brand-blue)"/>
    <polyline points="340,302 368,331 340,360" fill="none" stroke="var(--paper)" stroke-width="7"/>
  </svg>
  <div class="brand">
    <span class="brand__dot"></span>
    <span class="brand__name">Bugwarden</span>
  </div>
</section>

<section class="card card--back" aria-label="Business card back">
  <svg class="bands" width="700" height="400" viewBox="0 0 700 400" aria-hidden="true">
    <rect x="0" y="160" width="700" height="56" fill="var(--brand-blue)"/>
    <polyline points="225,160 252,188 225,216" fill="none" stroke="var(--paper)" stroke-width="7"/>
    <polyline points="465,160 492,188 465,216" fill="none" stroke="var(--paper)" stroke-width="7"/>
    <!-- globe -->
    <g class="icon-globe" fill="none" stroke="var(--paper)" stroke-width="2">
      <circle cx="70" cy="188" r="13"/>
      <ellipse cx="70" cy="188" rx="6" ry="13"/>
      <line x1="57" y1="188" x2="83" y2="188"/>
      <line x1="59" y1="181" x2="81" y2="181"/>
      <line x1="59" y1="195" x2="81" y2="195"/>
    </g>
    <!-- pin -->
    <g class="icon-pin">
      <path d="M358 174 a11 11 0 0 1 11 11 c0 9 -11 19 -11 19 c0 0 -11 -10 -11 -19 a11 11 0 0 1 11 -11 z" fill="var(--paper)"/>
      <circle cx="358" cy="185" r="4" fill="var(--brand-blue)"/>
    </g>
    <!-- phone -->
    <g class="icon-phone">
      <rect x="600" y="172" width="18" height="32" rx="3" fill="none" stroke="var(--paper)" stroke-width="2.5"/>
      <circle cx="609" cy="199" r="1.8" fill="var(--paper)"/>
    </g>
    <rect x="0" y="342" width="700" height="58" fill="var(--brand-red)"/>
  </svg>

  <div class="brand">
    <span class="brand__dot"></span>
    <span class="brand__name">Bugwarden</span>
  </div>

  <div class="person">
    <p class="person__name">MALCOLM TEAGUE</p>
    <p class="person__role">GENERAL MANAGER</p>
  </div>

  <div class="contact contact--web">
    <p>info@bugwarden.example</p>
    <p>bugwarden.example</p>
  </div>
  <div class="contact contact--address">
    <p>047 12th floor Hall</p>
    <p>Marrow Road QTN</p>
  </div>
  <div class="contact contact--phone">
    <p>012 555 0147</p>
    <p>012 555 0147</p>
  </div>
</section>

</body>
</html>
```